Lawn sign for construction company

Would like this to be a very clean and high end design for luxury homes. We need a yard sign designed that includes the company logo, website, phone number and major service offerings (residential and commercial renovations and maintenance)
The company website is brambleworks.com all other contact info is in the attachments
Target Market(s)
Luxury home owners and business owners
Industry/Entity Type
Construction/Home Improvement
Font styles to use
Other font styles liked:
- See company logo and other graphics included for title text fonts. All other fonts can be standard sans serif.
Colors
0054AA
0677BA
7BADD7
CADEEF
E8F1F8
Requirements
Must have
- Clean, easy to read design, would like 2 sided sign. A main sign side and back side which states “free estimates, and includes the website and phone number. Must also match the color scheme of the provided logo and other company images. Dark Navy blue primary color, gray secondary color, and orange as an accent color.
Nice to have
- 2nd sign side very simple design
Should not have
- Too many graphics limit to 1-3 colors

```html
<!DOCTYPE html>
<html lang="en">
<head>
<meta charset="utf-8">
<title>Yard Sign – Front and Back</title>
<link rel="stylesheet" href="https://fonts.googleapis.com/css2?family=Montserrat:wght@400;700;800&display=swap">
<style>
  :root {
    --backdrop: #767474;
    --panel-dark: #cbcbcb;
    --panel-light: #dcdcdc;
    --navy: #040b5e;
    --orange: #e8780f;
    --slate: #6a6a6a;
    --ink: #2e2e2e;
    --white: #ffffff;
  }
  * { box-sizing: border-box; margin: 0; padding: 0; }
  html, body { width: 1200px; height: 1200px; overflow: hidden; }
  body {
    background: var(--backdrop);
    font-family: "Montserrat", sans-serif;
    position: relative;
  }
  .sign {
    position: absolute;
    left: 224px;
    width: 752px;
    height: 501px;
    background: linear-gradient(to bottom right, var(--panel-dark) 50%, var(--panel-light) 50%);
  }
  .sign--front { top: 71px; }
  .sign--back { top: 627px; }

  .sign__frame {
    position: absolute;
    left: 17px; right: 17px; top: 13px; bottom: 13px;
    border: 1.5px solid var(--navy);
  }
  .headline {
    position: absolute;
    top: 28px; left: 0; right: 0;
    text-align: center;
    font-weight: 800;
    font-size: 72px;
    line-height: 64px;
    letter-spacing: -1px;
    color: var(--navy);
  }
  .headline__accent { color: var(--orange); }

  .brand {
    position: absolute;
    left: 0; right: 0;
    display: flex;
    align-items: center;
    justify-content: center;
    gap: 14px;
    font-weight: 800;
    color: var(--orange);
    letter-spacing: 1px;
  }
  .brand__mark {
    width: 26px; height: 26px;
    background: var(--navy);
  }
  .sign--front .brand { top: 200px; font-size: 44px; line-height: 60px; }
  .sign--back .brand { top: 142px; font-size: 48px; line-height: 64px; }
  .sign--back .brand__mark { width: 30px; height: 30px; }

  .contact-band {
    position: absolute;
    left: 17px; right: 17px; top: 366px; bottom: 13px;
    background: var(--navy);
    text-align: center;
  }
  .contact-band__phone {
    display: flex;
    align-items: center;
    justify-content: center;
    gap: 12px;
    margin-top: 10px;
    font-weight: 700;
    font-size: 68px;
    line-height: 64px;
    color: var(--white);
  }
  .phone-icon { width: 46px; height: 46px; }
  .contact-band__web {
    margin-top: 4px;
    font-weight: 700;
    font-size: 29px;
    line-height: 34px;
    letter-spacing: 4px;
    color: var(--orange);
  }

  .contact-label {
    position: absolute;
    top: 332px; left: 0; right: 0;
    display: flex;
    align-items: center;
    justify-content: center;
    gap: 8px;
    font-size: 25px;
    line-height: 28px;
    color: var(--ink);
  }
  .contact-label::before, .contact-label::after {
    content: "";
    width: 26px;
    border-top: 1.5px solid var(--ink);
  }
  .contact-number {
    position: absolute;
    top: 355px; left: 0; right: 0;
    text-align: center;
    font-weight: 700;
    font-size: 58px;
    line-height: 64px;
    color: var(--navy);
  }
  .rule {
    position: absolute;
    top: 420px; left: 88px; right: 90px;
    border-top: 1.5px solid var(--navy);
  }
  .services {
    position: absolute;
    top: 428px; left: 0; right: 0;
    text-align: center;
    font-weight: 700;
    font-size: 23.5px;
    line-height: 26px;
    color: var(--slate);
    letter-spacing: 0.3px;
  }
  .services__dot {
    display: inline-block;
    width: 13px; height: 13px;
    background: var(--orange);
    margin: 0 6px;
    vertical-align: 2px;
  }
</style>
</head>
<body>

<section class="sign sign--front">
  <div class="sign__frame"></div>
  <h1 class="headline"><span class="headline__accent">FREE</span> ESTIMATES</h1>
  <div class="brand"><span class="brand__mark"></span>HARROW BUILD CO.</div>
  <div class="contact-band">
    <div class="contact-band__phone">
      <svg class="phone-icon" viewBox="0 0 48 48" aria-hidden="true">
        <path d="M10 6c2-1 4 0 5 2l4 7c1 2 0 3-1 4l-3 2c2 5 6 9 11 11l2-3c1-1 2-2 4-1l7 4c2 1 3 3 2 5l-2 4c-1 2-3 3-5 3C18 44 4 30 4 14c0-2 1-4 3-5z" fill="#e8780f"/>
        <path d="M28 4a16 16 0 0 1 16 16M28 10a10 10 0 0 1 10 10M28 16a4 4 0 0 1 4 4" fill="none" stroke="#e8780f" stroke-width="2.5" stroke-linecap="round"/>
      </svg>
      800-555-0142
    </div>
    <div class="contact-band__web">www.brambleworks.com</div>
  </div>
</section>

<section class="sign sign--back">
  <div class="brand"><span class="brand__mark"></span>HARROW BUILD CO.</div>
  <p class="contact-label">CONTACT US ON</p>
  <p class="contact-number">800.555.0142</p>
  <div class="rule"></div>
  <p class="services">
    RESIDENTIAL RENOVATIONS<span class="services__dot"></span>COMMERCIAL<br>
    RENOVATIONS<span class="services__dot"></span>MAINTENANCE
  </p>
</section>

</body>
</html>
```